Irrigation Business needs their business cards modernised and revamped

I would like to keep my current logo, colours and revamp the format of the card.

I would like the card to be clean yet important.

Im not sure if you include texture but i would like the named logo to be indented into the card etc.

show me something alive and free something thats clinical to the point yet has a feel of achievement. i would like people to go nice card.

Target Market(s)

high end clients, corporate, sports field manger, the guys that make the decisions

Industry/Entity Type

Business

Contact Information for Business Card

nformation to be included

Dorian Hesk (Director)
0487253916
dorian@tfcraft.biz
www.taddsfieldcrafts.com

instagram logo
google logo
facebook logo

Colors

Designer to choose colors to be used in the design.

Requirements
Nice to have
• indentations a really nice feel to the card good texture

```html
<!DOCTYPE html>
<html lang="en">
<head>
<meta charset="utf-8">
<title>Tadd's Field Crafts – Business Card</title>
<link rel="stylesheet" href="https://fonts.googleapis.com/css2?family=Montserrat:wght@700&family=Mulish:wght@400;600&display=swap">
<style>
  :root {
    --page: #ece9e6;
    --brand-blue: #2d67ad;
    --deep-blue: #2554a3;
    --sky-blue: #29a3dd;
    --leaf-green: #2a9a3f;
    --ink-grey: #5d6168;
    --card-white: #ffffff;
  }
  * { box-sizing: border-box; margin: 0; padding: 0; }
  html, body { width: 1200px; height: 715px; overflow: hidden; background: var(--page); }
  .canvas {
    position: relative; width: 1200px; height: 715px;
    display: flex; align-items: center; justify-content: center; gap: 40px;
  }
  .card {
    position: relative; width: 540px; height: 310px; overflow: hidden;
    box-shadow: 0 10px 26px rgba(0,0,0,.18);
  }
  /* Back of card */
  .card-back {
    background: var(--brand-blue); color: var(--card-white);
    display: flex; flex-direction: column; align-items: center; justify-content: center;
  }
  .brand-mark { display: flex; flex-direction: column; align-items: center; gap: 10px; }
  .brand-dot { width: 46px; height: 46px; border-radius: 50%; background: currentColor; }
  .brand-name {
    font-family: "Montserrat", sans-serif; font-weight: 700;
    font-size: 24px; letter-spacing: .5px; text-transform: uppercase;
  }
  .back-web {
    position: absolute; bottom: 52px; left: 0; right: 0; text-align: center;
    font-family: "Mulish", sans-serif; font-size: 12px; letter-spacing: .3px;
  }
  /* Front of card */
  .card-front { background: var(--card-white); font-family: "Mulish", sans-serif; }
  .name-tab {
    position: absolute; left: 0; top: 52px; width: 8px; height: 34px;
    background: var(--sky-blue); border-radius: 0 8px 8px 0;
  }
  .person { position: absolute; left: 40px; top: 52px; }
  .person-name {
    font-family: "Montserrat", sans-serif; font-weight: 700;
    color: var(--brand-blue); font-size: 18px; text-transform: uppercase; letter-spacing: .3px;
  }
  .person-title { color: var(--ink-grey); font-size: 12px; margin-top: 2px; }
  .divider {
    position: absolute; left: 40px; right: 40px; top: 104px;
    height: 1px; background: var(--leaf-green);
  }
  .contacts { position: absolute; left: 40px; top: 120px; list-style: none; }
  .contacts li {
    display: flex; align-items: center; gap: 10px;
    color: var(--ink-grey); font-size: 12.5px; line-height: 20px;
  }
  .contacts svg { width: 11px; height: 11px; fill: var(--brand-blue); flex: none; }
  .front-brand {
    position: absolute; right: 40px; top: 122px;
    color: var(--brand-blue); align-items: flex-end;
  }
  .front-brand .brand-dot { width: 38px; height: 38px; margin-right: 50px; }
  .front-brand .brand-name { font-size: 17px; }
  .social { position: absolute; right: 40px; bottom: 40px; display: flex; gap: 7px; }
  .social span { width: 13px; height: 13px; border-radius: 50%; background: var(--brand-blue); }
  .band { position: absolute; bottom: 0; height: 12px; }
  .band-light { left: 0; width: 290px; background: var(--sky-blue); clip-path: polygon(0 0, 100% 0, 97% 100%, 0 100%); }
  .band-dark { right: 0; width: 252px; background: var(--deep-blue); clip-path: polygon(4% 0, 100% 0, 100% 100%, 0 100%); }
</style>
</head>
<body>
<main class="canvas">
  <section class="card card-back">
    <div class="brand-mark">
      <span class="brand-dot"></span>
      <span class="brand-name">Tadd's Field Crafts</span>
    </div>
    <p class="back-web">www.taddsfieldcrafts.com</p>
  </section>

  <section class="card card-front">
    <span class="name-tab"></span>
    <div class="person">
      <h1 class="person-name">Dorian Hesk</h1>
      <p class="person-title">Director</p>
    </div>
    <span class="divider"></span>
    <ul class="contacts">
      <li><svg viewBox="0 0 24 24"><path d="M6.6 10.8a15 15 0 0 0 6.6 6.6l2.2-2.2c.3-.3.7-.4 1-.2 1.1.4 2.3.6 3.6.6.6 0 1 .4 1 1V20c0 .6-.4 1-1 1A17 17 0 0 1 3 4c0-.6.4-1 1-1h3.5c.6 0 1 .4 1 1 0 1.3.2 2.5.6 3.6.1.3 0 .7-.2 1z"/></svg>0487253916</li>
      <li><svg viewBox="0 0 24 24"><path d="M2 5h20v14H2zm2 2v.5l8 5 8-5V7l-8 5z"/></svg>dorian@tfcraft.biz</li>
      <li><svg viewBox="0 0 24 24"><path d="M12 2a10 10 0 1 0 0 20 10 10 0 0 0 0-20zm6.9 9h-3a15 15 0 0 0-1.3-6 8 8 0 0 1 4.3 6zM12 4c1 1.3 1.8 3.9 1.9 7h-3.8c.1-3.1.9-5.7 1.9-7zM9.4 5a15 15 0 0 0-1.3 6h-3a8 8 0 0 1 4.3-6zM5.1 13h3a15 15 0 0 0 1.3 6 8 8 0 0 1-4.3-6zM12 20c-1-1.3-1.8-3.9-1.9-7h3.8c-.1 3.1-.9 5.7-1.9 7zm2.6-1a15 15 0 0 0 1.3-6h3a8 8 0 0 1-4.3 6z"/></svg>taddsfieldcrafts.com</li>
    </ul>
    <div class="brand-mark front-brand">
      <span class="brand-dot"></span>
      <span class="brand-name">Tadd's Field Crafts</span>
    </div>
    <div class="social" aria-label="Social media links">
      <span></span><span></span><span></span>
    </div>
    <span class="band band-light"></span>
    <span class="band band-dark"></span>
  </section>
</main>
</body>
</html>
```